" SOMOS UMA CANTINA ESCOLAR, PORÉM TEMOS PLANOS DE EXPANSÃO E PARA ISSO BUSCAMOS CRIAR UMA MARCA QUE SERÁ O NOME USADO EM TODAS AS CANTINAS ADMINISTRADAS POR NOSSA EMPRESA. "

```html
<!DOCTYPE html>
<html lang="pt-BR">
<head>
<meta charset="utf-8">
<title>Recreio Cantinas Escolares – Cartão de visita</title>
<link rel="stylesheet" href="https://fonts.googleapis.com/css2?family=Montserrat:wght@600;700;800&family=Open+Sans:wght@400;600&display=swap">
<style>
  :root {
    --backdrop: #d3d3d3;
    --brand-red: #b51f2a;
    --brand-red-deep: #8e1820;
    --brand-yellow: #f3b50a;
    --paper: #ffffff;
    --ink-red: #a51d26;
  }
  * { margin: 0; padding: 0; box-sizing: border-box; }
  html, body { width: 1200px; height: 1200px; overflow: hidden; }
  body { background: var(--backdrop); position: relative; font-family: "Open Sans", sans-serif; }

  .card {
    position: absolute;
    left: 271px;
    width: 658px;
    height: 365px;
    overflow: hidden;
  }
  .card--front { top: 204px; }
  .card--back { top: 636px; background: var(--paper); }

  .card__photo {
    position: absolute; inset: 0;
    background: linear-gradient(120deg, var(--brand-red-deep) 0%, var(--brand-red) 45%, #c8333a 70%, var(--brand-red-deep) 100%);
  }
  .card__swoosh { position: absolute; inset: 0; }

  .wordmark {
    font-family: "Montserrat", sans-serif;
    font-weight: 800;
    line-height: 1;
    letter-spacing: 0.01em;
  }
  .tagline {
    font-family: "Montserrat", sans-serif;
    font-weight: 600;
    text-transform: uppercase;
    letter-spacing: 0.34em;
  }

  .front-brand {
    position: absolute; left: 0; width: 100%; top: 132px;
    text-align: center; color: var(--paper);
  }
  .front-brand .wordmark { font-size: 58px; }
  .front-brand .tagline { font-size: 15px; margin-top: 6px; }

  .back-brand {
    position: absolute; left: 36px; top: 112px; width: 200px;
    text-align: center; color: var(--ink-red);
  }
  .back-brand .wordmark { font-size: 36px; }
  .back-brand .tagline { font-size: 9.5px; margin-top: 4px; letter-spacing: 0.3em; }

  .contact {
    position: absolute; right: 36px; text-align: right;
    color: var(--ink-red); font-weight: 600; font-size: 17px; line-height: 1.55;
  }
  .contact--reach { top: 82px; }
  .contact--address { top: 168px; }

  .web-band { position: absolute; right: 0; top: 281px; width: 370px; height: 27px; }
  .web-band__text {
    position: absolute; right: 24px; top: 281px; height: 27px; line-height: 27px;
    color: var(--paper); font-size: 14px; font-weight: 600; letter-spacing: 0.22em;
  }
  .back-arc { position: absolute; left: 0; top: 0; }
</style>
</head>
<body>

<section class="card card--front" aria-label="Frente do cartão">
  <div class="card__photo" role="img" aria-label="Foto de crianças lanchando na cantina da escola, com tom vermelho"></div>
  <svg class="card__swoosh" width="658" height="365" viewBox="0 0 658 365" aria-hidden="true">
    <path d="M520 0 C 500 170 380 300 190 365 L 360 365 C 520 290 610 160 658 40 L 658 0 Z" fill="var(--brand-yellow)" opacity="0.72"/>
  </svg>
  <div class="front-brand">
    <div class="wordmark">RECREIO</div>
    <div class="tagline">Cantinas Escolares</div>
  </div>
</section>

<section class="card card--back" aria-label="Verso do cartão">
  <div class="back-brand">
    <div class="wordmark">RECREIO</div>
    <div class="tagline">Cantinas Escolares</div>
  </div>

  <address class="contact contact--reach" style="font-style:normal">
    (48) 3010-2020<br>
    contato@cantinasrecreio.com.br
  </address>
  <address class="contact contact--address" style="font-style:normal">
    Rua das Palmeiras, n.º 210 / sala 04<br>
    Centro / Vila Nova / SC<br>
    CEP: 88000-000
  </address>

  <svg class="back-arc" width="658" height="365" viewBox="0 0 658 365" aria-hidden="true">
    <path d="M86 365 C 92 310 118 262 160 232" fill="none" stroke="var(--brand-yellow)" stroke-width="26"/>
  </svg>

  <svg class="web-band" width="370" height="27" viewBox="0 0 370 27" aria-hidden="true">
    <path d="M10 0 L370 0 L370 27 L0 27 Z" fill="var(--brand-yellow)"/>
  </svg>
  <div class="web-band__text">www.cantinasrecreio.com.br</div>
</section>

</body>
</html>
```